Spacer for Aerosol design - Breathwell Orbit Spacer

Require outer box design for Spacer for Aerosol inhaler- Pharmaceutical medical device require high ended design and professional as promoting to Doctor and Pharmacies in UK.

Enclosed Design outline and similar products available in market with variations required.

For more info require about design email- info@kelvashealth.co.uk

1) Name of Products and colour variation in product as below

No Product Colour of Device
1 BreathWell Orbit Adult Blue
2 BreathWell Orbit Adult with mask Blue
3 BreathWell Orbit with Child mask Yellow
4 BreathWell Orbit with Infant mask Orange

2) Colour of box variation require with product colour change i.e. blue, yellow and orange (not whole box colour but strip or lining to indicate diff product)
3) Box dimensions 170 X 80 X 80 mm
4) Spacer design (content) need to be on box with different colour with product variance as product with colour

Target Market(s)

UK

Industry/Entity Type

Pharmaceutical

Colors

Designer to choose colors to be used in the design.

Requirements
Must have
• Professional design as promoting as medical device
Nice to have
• variance in design and graphics

```html
<!DOCTYPE html>
<html lang="en">
<head>
<meta charset="utf-8">
<title>BreathWell Orbit Spacer – Box Panels</title>
<link href="https://fonts.googleapis.com/css2?family=Ubuntu:wght@500;700&family=PT+Sans+Narrow:wght@400;700&display=swap" rel="stylesheet">
<style>
  :root {
    --bg: #e9ebec;
    --paper: #f4f4f2;
    --ink: #3e4042;
    --ink-soft: #5a5c5e;
    --brand: #5aa832;
    --blue: #1f78c1;
    --blue-light: #5db0e4;
    --yellow: #f0c419;
    --yellow-light: #f8e27a;
    --orange: #e57f2c;
    --orange-light: #f4b27a;
  }
  * { box-sizing: border-box; margin: 0; padding: 0; }
  html, body { width: 1200px; height: 1200px; overflow: hidden; }
  body { background: var(--bg); font-family: "Ubuntu", sans-serif; color: var(--ink); position: relative; }

  .panel {
    position: absolute;
    background: var(--paper);
    overflow: hidden;
    box-shadow: 0 2px 6px rgba(0,0,0,.12);
  }
  .front { width: 270px; height: 575px; top: 35px; }
  .side  { width: 270px; height: 535px; top: 640px; }

  .infant { --accent: var(--orange); --accent-light: var(--orange-light); }
  .child  { --accent: var(--yellow); --accent-light: var(--yellow-light); }
  .adult  { --accent: var(--blue);   --accent-light: var(--blue-light); }

  .art { position: absolute; inset: 0; }

  .brand {
    position: absolute; top: 34px; left: 0; right: 0;
    display: flex; align-items: center; justify-content: center; gap: 8px;
    font-family: "Ubuntu", sans-serif; font-weight: 500; font-size: 15px; color: var(--brand);
  }
  .brand-dot { width: 16px; height: 16px; border-radius: 50%; border: 3px solid var(--brand); }

  .title {
    position: absolute; top: 96px; left: 22px; right: 12px;
    font-weight: 700; font-size: 33px; line-height: 1.08; color: var(--ink);
  }
  .title .sub { display: block; font-size: 23px; margin-top: 4px; }

  .device {
    position: absolute; left: 140px; top: 300px; width: 92px; height: 250px;
    border-radius: 22px 22px 8px 8px;
    background: linear-gradient(90deg, rgba(255,255,255,.95), rgba(220,228,235,.9) 60%, rgba(255,255,255,.95));
    border: 1px solid rgba(150,165,180,.5);
    box-shadow: inset 0 -26px 0 var(--accent-light), inset 0 30px 0 var(--accent);
  }

  .badge {
    position: absolute; left: 20px; top: 462px; width: 88px; height: 88px; border-radius: 50%;
    background: var(--paper); border: 5px solid var(--accent);
    display: flex; align-items: center; justify-content: center; text-align: center;
    font-weight: 700; font-size: 15px; line-height: 1.05; color: var(--accent);
  }

  /* instructions */
  .instructions h2 {
    position: absolute; top: 28px; left: 22px;
    font-family: "PT Sans Narrow", sans-serif; font-weight: 700; font-size: 27px; color: var(--ink);
  }
  .step { position: absolute; left: 18px; right: 16px; display: flex; gap: 12px; align-items: flex-start; }
  .step-pic {
    flex: 0 0 96px; height: 96px; border-radius: 50%;
    border: 6px solid var(--accent);
    background: radial-gradient(circle, #ffffff, var(--accent-light));
  }
  .step p {
    font-family: "PT Sans Narrow", sans-serif; font-size: 15px; line-height: 1.22; color: var(--ink-soft);
  }
  .step:nth-of-type(1) { top: 92px; }
  .step:nth-of-type(2) { top: 235px; }
  .step:nth-of-type(3) { top: 378px; }
  .instructions .strip { position: absolute; left: 0; right: 0; bottom: 0; height: 14px; background: var(--accent); }

  /* features */
  .features .feat-title {
    position: absolute; top: 88px; left: 22px;
    font-family: "PT Sans Narrow", sans-serif; font-weight: 700; font-size: 34px; line-height: 1.02; color: var(--ink);
  }
  .features ul { position: absolute; top: 180px; left: 24px; list-style: none; }
  .features li {
    font-family: "PT Sans Narrow", sans-serif; font-size: 19px; color: var(--ink);
    padding-left: 18px; position: relative; margin-bottom: 9px;
  }
  .features li::before {
    content: ""; position: absolute; left: 0; top: 7px; width: 8px; height: 8px; border-radius: 50%; background: var(--accent);
  }
  .features .device { left: 190px; top: 350px; width: 46px; height: 150px; border-radius: 12px 12px 5px 5px;
    box-shadow: inset 0 -14px 0 var(--accent-light), inset 0 16px 0 var(--accent); }
  .features .strip { position: absolute; left: 0; right: 0; bottom: 0; height: 14px; background: var(--accent); }
</style>
</head>
<body>

<!-- Front panels -->
<section class="panel front infant" style="left:30px">
  <svg class="art" viewBox="0 0 270 575" aria-hidden="true">
    <path d="M40 600 C 40 430 150 360 290 385" fill="none" stroke="var(--accent)" stroke-width="56"/>
    <circle cx="60" cy="265" r="22" fill="var(--accent)" opacity=".75"/>
    <circle cx="200" cy="240" r="14" fill="var(--accent)" opacity=".55"/>
    <circle cx="110" cy="320" r="13" fill="none" stroke="var(--accent)" stroke-width="5" opacity=".8"/>
    <circle cx="35" cy="350" r="9" fill="var(--accent)"/>
    <circle cx="240" cy="285" r="7" fill="var(--accent)" opacity=".6"/>
    <circle cx="95" cy="410" r="16" fill="var(--accent-light)" opacity=".8"/>
  </svg>
  <div class="brand"><span class="brand-dot"></span>Kelvas Health</div>
  <h1 class="title">BreathWell<br>Orbit<span class="sub">with Infant mask</span></h1>
  <div class="device" role="img" aria-label="Clear spacer chamber with orange infant mask"></div>
  <div class="badge">Infant</div>
</section>

<section class="panel front child" style="left:320px">
  <svg class="art" viewBox="0 0 270 575" aria-hidden="true">
    <path d="M40 600 C 40 430 150 360 290 385" fill="none" stroke="var(--accent)" stroke-width="56"/>
    <circle cx="55" cy="270" r="24" fill="var(--accent-light)" opacity=".85"/>
    <circle cx="115" cy="240" r="10" fill="var(--accent)" opacity=".6"/>
    <circle cx="210" cy="250" r="15" fill="var(--accent-light)"/>
    <circle cx="100" cy="330" r="14" fill="none" stroke="var(--accent)" stroke-width="5" opacity=".8"/>
    <circle cx="35" cy="370" r="9" fill="var(--accent)"/>
    <circle cx="95" cy="420" r="18" fill="var(--accent-light)" opacity=".8"/>
  </svg>
  <div class="brand"><span class="brand-dot"></span>Kelvas Health</div>
  <h1 class="title">BreathWell<br>Orbit Child<span class="sub">with mask</span></h1>
  <div class="device" role="img" aria-label="Clear spacer chamber with yellow child mask"></div>
  <div class="badge">6 years<br>and +</div>
</section>

<section class="panel front adult" style="left:610px">
  <svg class="art" viewBox="0 0 270 575" aria-hidden="true">
    <path d="M40 600 C 40 430 150 360 290 385" fill="none" stroke="var(--accent)" stroke-width="56"/>
    <circle cx="40" cy="270" r="9" fill="var(--accent-light)"/>
    <circle cx="80" cy="300" r="22" fill="var(--accent)" opacity=".85"/>
    <circle cx="130" cy="240" r="12" fill="none" stroke="var(--accent-light)" stroke-width="4"/>
    <circle cx="220" cy="225" r="9" fill="var(--accent)" opacity=".7"/>
    <circle cx="45" cy="360" r="13" fill="none" stroke="var(--accent)" stroke-width="5"/>
    <circle cx="110" cy="370" r="14" fill="var(--accent-light)" opacity=".8"/>
    <circle cx="60" cy="430" r="10" fill="var(--accent)"/>
  </svg>
  <div class="brand"><span class="brand-dot"></span>Kelvas Health</div>
  <h1 class="title">BreathWell<br>Orbit Adult</h1>
  <div class="device" role="img" aria-label="Clear spacer chamber with blue cap and base"></div>
  <div class="badge">6 years<br>&amp;<br>adult</div>
</section>

<section class="panel front adult" style="left:900px">
  <svg class="art" viewBox="0 0 270 575" aria-hidden="true">
    <path d="M40 600 C 40 430 150 360 290 385" fill="none" stroke="var(--accent)" stroke-width="56"/>
    <circle cx="60" cy="255" r="11" fill="var(--accent)" opacity=".7"/>
    <circle cx="200" cy="235" r="16" fill="none" stroke="var(--accent-light)" stroke-width="4"/>
    <circle cx="95" cy="310" r="20" fill="var(--accent-light)" opacity=".85"/>
    <circle cx="40" cy="380" r="12" fill="none" stroke="var(--accent)" stroke-width="5"/>
    <circle cx="110" cy="420" r="9" fill="var(--accent)"/>
  </svg>
  <div class="brand"><span class="brand-dot"></span>Kelvas Health</div>
  <h1 class="title">BreathWell<br>Orbit Adult<span class="sub">with mask</span></h1>
  <div class="device" role="img" aria-label="Clear spacer chamber with blue cap and adult mask"></div>
  <div class="badge">6 years<br>&amp;<br>adult</div>
</section>

<!-- Side panels -->
<section class="panel side instructions infant" style="left:30px">
  <h2>Instructions for use</h2>
  <div class="step"><div class="step-pic" role="img" aria-label="Step illustration: inserting the inhaler"></div><p>Remove the cap and shake the inhaler, hold it upright and insert it into the base of the spacer.</p></div>
  <div class="step"><div class="step-pic" role="img" aria-label="Step illustration: fitting the mask"></div><p>Place the mouthpiece between your lips or fit the mask over nose and mouth. Press the inhaler once and breathe in slowly.</p></div>
  <div class="step"><div class="step-pic" role="img" aria-label="Step illustration: removing the inhaler"></div><p>Wait one minute before the next dose. Remove the inhaler and replace the cap. Rinse your mouth.</p></div>
  <div class="strip"></div>
</section>

<section class="panel side instructions child" style="left:320px">
  <h2>Instructions for use</h2>
  <div class="step"><div class="step-pic" role="img" aria-label="Step illustration: inserting the inhaler"></div><p>Remove the cap and shake the inhaler, hold it upright and insert it into the base of the spacer.</p></div>
  <div class="step"><div class="step-pic" role="img" aria-label="Step illustration: fitting the mask"></div><p>Place the mouthpiece between your lips or fit the mask over nose and mouth. Press the inhaler once and breathe in slowly.</p></div>
  <div class="step"><div class="step-pic" role="img" aria-label="Step illustration: removing the inhaler"></div><p>Wait one minute before the next dose. Remove the inhaler and replace the cap. Rinse your mouth.</p></div>
  <div class="strip"></div>
</section>

<section class="panel side instructions adult" style="left:610px">
  <h2>Instructions for use</h2>
  <div class="step"><div class="step-pic" role="img" aria-label="Step illustration: inserting the inhaler"></div><p>Remove the cap and shake the inhaler, hold it upright and insert it into the base of the spacer.</p></div>
  <div class="step"><div class="step-pic" role="img" aria-label="Step illustration: using the mouthpiece"></div><p>Place the mouthpiece between your lips or fit the mask over nose and mouth. Press the inhaler once and breathe in slowly.</p></div>
  <div class="step"><div class="step-pic" role="img" aria-label="Step illustration: removing the inhaler"></div><p>Wait one minute before the next dose. Remove the inhaler and replace the cap. Rinse your mouth.</p></div>
  <div class="strip"></div>
</section>

<section class="panel side features adult" style="left:900px">
  <div class="brand"><span class="brand-dot"></span>Kelvas Health</div>
  <h2 class="feat-title">BreathWell<br>Orbit Adult</h2>
  <ul>
    <li>Visual valve</li>
    <li>Anti-microbial valve</li>
    <li>Universal base</li>
    <li>Reusable</li>
    <li>Antistatic</li>
    <li>BPA and latex-free</li>
    <li>Optional silicon mask</li>
  </ul>
  <div class="device" role="img" aria-label="Small spacer chamber with blue cap"></div>
  <div class="strip"></div>
</section>

</body>
</html>
```